Puff'nTidy Cat Litter Logo/Package Concept

We need a logo and packaging design concept for a new brand of paper cat littler.

The product is a paper cat litter that utilises special technology to offer superior Odour and moisture absorption - making it more pleasant for customers to clean and have in their home.

It is also Biodegradable and made from Recycled Material so it is friendly to the environment and customers can feel good that they are making an ethical, responsible choice for their cat's litter.

The litter granules are also particularly appealing to cats.

Target Market(s)

Females 25-45 years, cat owners

Industry/Entity Type

Pet Care

Colors
fbed22
9bcb3b
00a990
0492cd
266eb0
6a439a

Requirements
Must have
• - A concept for the Puff'nTidy logo
• - Product title in a large, prominent spot on the front "Paper"
• - Feel; clean, fresh, crisp, simple, inviting, anti-bacterial, sparkling, bright,
• - A close-up picture of the actual litter granules
• - A caricature of a cat OR a photo of a real cat.
• - image imposed on a 3D bag, example supplied. Can use alternative image if preferred.
Nice to have
• The ability for the design to be adapted to expand into crystal/clay littler once we introduce more products into the range.
Should not have
• anything to do with dogs
• feel to natural, holistic, earthy or dull.

```html
<!DOCTYPE html>
<html lang="en">
<head>
<meta charset="utf-8">
<title>Puff'nTidy Litter Range – Pack Fronts</title>
<link rel="stylesheet" href="https://fonts.googleapis.com/css2?family=Montserrat:wght@700;800&display=swap">
<style>
  :root {
    --artboard-bg: #4f4f4f;
    --pack-teal: #12a891;
    --brand-yellow: #f8ea26;
    --white: #ffffff;
    --label-ink: #0d8a77;
    --crystal-pink: #c94a8b;
    --clay-purple: #782b88;
    --paper-orange: #f36c17;
    --granule-light: #d7cdb4;
    --granule-dark: #8f8470;
    --cat-light: #f2c27c;
    --cat-dark: #c9823a;
  }
  * { box-sizing: border-box; margin: 0; padding: 0; }
  html, body { width: 1200px; height: 536px; overflow: hidden; }
  body {
    background: var(--artboard-bg);
    font-family: "Montserrat", Arial, sans-serif;
    position: relative;
  }
  .pack {
    position: absolute;
    top: 10px;
    width: 384px;
    height: 519px;
    background: var(--pack-teal);
    overflow: hidden;
  }
  .pack--crystal { left: 8px; }
  .pack--clay { left: 406px; }
  .pack--paper { left: 813px; }

  .pack__pattern {
    position: absolute; inset: 0;
    background: radial-gradient(circle at 50% 40%, rgba(255,255,255,0.04), rgba(0,0,0,0.04));
  }
  .brand-name {
    position: absolute; top: 30px; left: 0; right: 0;
    text-align: center;
    color: var(--brand-yellow);
    font-weight: 800;
    font-size: 38px;
    letter-spacing: -0.5px;
    line-height: 1;
  }
  .range-band {
    position: absolute; left: 22px; top: 100px;
    width: 342px; height: 66px;
    border-radius: 4px;
  }
  .pack--crystal .range-band { background: var(--crystal-pink); }
  .pack--clay .range-band { background: var(--clay-purple); }
  .pack--paper .range-band { background: var(--paper-orange); }
  .range-title {
    position: absolute; left: 0; right: 0; top: 96px;
    text-align: center;
    color: var(--white);
    font-weight: 800;
    font-size: 66px;
    line-height: 74px;
    letter-spacing: 0.5px;
  }
  .product-line {
    position: absolute; left: 0; right: 0; top: 190px;
    text-align: center;
    color: var(--white);
    font-weight: 800;
    font-size: 44px;
    line-height: 1;
  }
  .cat-photo {
    position: absolute; left: 66px; top: 362px;
    width: 306px; height: 170px;
    border-radius: 140px 140px 0 0;
    background: linear-gradient(180deg, var(--cat-light), var(--cat-dark));
  }
  .granules-photo {
    position: absolute; left: 130px; top: 268px;
    width: 124px; height: 124px;
    border-radius: 50%;
    border: 4px solid var(--brand-yellow);
    background: radial-gradient(circle, var(--granule-light), var(--granule-dark));
  }
  .connectors { position: absolute; inset: 0; pointer-events: none; }
  .feature-icon {
    position: absolute;
    width: 54px; height: 54px;
    border-radius: 50%;
    border: 2px solid var(--brand-yellow);
    background: var(--pack-teal);
    display: flex; align-items: center; justify-content: center;
  }
  .feature-icon svg { width: 30px; height: 30px; }
  .feature-icon--recycle { left: 34px; top: 262px; }
  .feature-icon--odour { left: 320px; top: 273px; }
  .feature-icon--moisture { left: 295px; top: 343px; }
  .feature-icon--mineral { left: 10px; top: 393px; }

  .feature-label {
    position: absolute;
    display: flex; align-items: center; justify-content: center;
    text-align: center;
    font-weight: 700;
    font-size: 8.6px;
    line-height: 1.15;
    color: var(--label-ink);
    border-radius: 6px;
    padding: 3px 4px;
  }
  .feature-label--white { background: var(--white); }
  .feature-label--yellow { background: var(--brand-yellow); }
  .feature-label--recycle { left: 12px; top: 305px; width: 98px; height: 46px; }
  .feature-label--odour { left: 240px; top: 290px; width: 82px; height: 30px; }
  .feature-label--moisture { left: 282px; top: 390px; width: 98px; height: 50px; font-size: 9px; }
  .feature-label--mineral { left: 60px; top: 402px; width: 90px; height: 38px; }
</style>
</head>
<body>

<!-- Reusable pack front; range variants differ by band colour and title -->
<section class="pack pack--crystal">
  <div class="pack__pattern"></div>
  <div class="brand-name">PUFF'NTIDY</div>
  <div class="range-band"></div>
  <h1 class="range-title">CRYSTAL</h1>
  <h2 class="product-line">CAT LITTER</h2>
  <div class="cat-photo" role="img" aria-label="Photo of a ginger kitten peeking up from the bottom of the pack"></div>
  <div class="granules-photo" role="img" aria-label="Close-up photo of litter granules"></div>
  <svg class="connectors" viewBox="0 0 384 519">
    <g fill="none" stroke="#f8ea26" stroke-width="2" stroke-linecap="round">
      <path d="M110 336 Q124 346 132 344"/><path d="M127 340 L133 344 L126 348"/>
      <path d="M240 306 L254 310"/>
      <path d="M300 372 Q270 360 246 362"/><path d="M252 358 L245 362 L252 366"/>
      <path d="M148 402 Q154 390 160 384"/>
    </g>
  </svg>
  <div class="feature-icon feature-icon--recycle"><svg viewBox="0 0 30 30" fill="none" stroke="#fff" stroke-width="2" stroke-linejoin="round"><path d="M15 4 L25 22 H5 Z"/><path d="M12 18 Q15 10 20 12"/></svg></div>
  <div class="feature-icon feature-icon--odour"><svg viewBox="0 0 30 30" fill="none" stroke="#fff" stroke-width="2" stroke-linecap="round"><path d="M8 24 Q4 18 8 14 Q12 10 8 5"/><path d="M15 24 Q11 18 15 14 Q19 10 15 5"/><path d="M22 24 Q18 18 22 14 Q26 10 22 5"/></svg></div>
  <div class="feature-icon feature-icon--moisture"><svg viewBox="0 0 30 30" fill="none" stroke="#fff" stroke-width="2"><path d="M15 4 Q23 15 23 19 A8 8 0 0 1 7 19 Q7 15 15 4 Z"/></svg></div>
  <div class="feature-icon feature-icon--mineral"><svg viewBox="0 0 30 30" fill="none" stroke="#fff" stroke-width="1.6"><circle cx="6" cy="6" r="2.5"/><circle cx="15" cy="6" r="2.5"/><circle cx="24" cy="6" r="2.5"/><circle cx="6" cy="15" r="2.5"/><circle cx="24" cy="15" r="2.5"/><circle cx="6" cy="24" r="2.5"/><circle cx="15" cy="24" r="2.5"/><circle cx="24" cy="24" r="2.5"/><path d="M8.5 6 H12.5 M17.5 6 H21.5 M6 8.5 V12.5 M24 17.5 V21.5 M8.5 24 H12.5"/></svg></div>
  <div class="feature-label feature-label--white feature-label--recycle">Biodegradable &amp; Made From Recycled Material</div>
  <div class="feature-label feature-label--yellow feature-label--odour">Superior Odour Absorption</div>
  <div class="feature-label feature-label--white feature-label--moisture">Superior Moisture Absorption</div>
  <div class="feature-label feature-label--yellow feature-label--mineral">Special mineral technology for superior freshness.</div>
</section>

<section class="pack pack--clay">
  <div class="pack__pattern"></div>
  <div class="brand-name">PUFF'NTIDY</div>
  <div class="range-band"></div>
  <h1 class="range-title">CLAY</h1>
  <h2 class="product-line">CAT LITTER</h2>
  <div class="cat-photo" role="img" aria-label="Photo of a ginger kitten peeking up from the bottom of the pack"></div>
  <div class="granules-photo" role="img" aria-label="Close-up photo of litter granules"></div>
  <svg class="connectors" viewBox="0 0 384 519">
    <g fill="none" stroke="#f8ea26" stroke-width="2" stroke-linecap="round">
      <path d="M110 336 Q124 346 132 344"/><path d="M127 340 L133 344 L126 348"/>
      <path d="M240 306 L254 310"/>
      <path d="M300 372 Q270 360 246 362"/><path d="M252 358 L245 362 L252 366"/>
      <path d="M148 402 Q154 390 160 384"/>
    </g>
  </svg>
  <div class="feature-icon feature-icon--recycle"><svg viewBox="0 0 30 30" fill="none" stroke="#fff" stroke-width="2" stroke-linejoin="round"><path d="M15 4 L25 22 H5 Z"/><path d="M12 18 Q15 10 20 12"/></svg></div>
  <div class="feature-icon feature-icon--odour"><svg viewBox="0 0 30 30" fill="none" stroke="#fff" stroke-width="2" stroke-linecap="round"><path d="M8 24 Q4 18 8 14 Q12 10 8 5"/><path d="M15 24 Q11 18 15 14 Q19 10 15 5"/><path d="M22 24 Q18 18 22 14 Q26 10 22 5"/></svg></div>
  <div class="feature-icon feature-icon--moisture"><svg viewBox="0 0 30 30" fill="none" stroke="#fff" stroke-width="2"><path d="M15 4 Q23 15 23 19 A8 8 0 0 1 7 19 Q7 15 15 4 Z"/></svg></div>
  <div class="feature-icon feature-icon--mineral"><svg viewBox="0 0 30 30" fill="none" stroke="#fff" stroke-width="1.6"><circle cx="6" cy="6" r="2.5"/><circle cx="15" cy="6" r="2.5"/><circle cx="24" cy="6" r="2.5"/><circle cx="6" cy="15" r="2.5"/><circle cx="24" cy="15" r="2.5"/><circle cx="6" cy="24" r="2.5"/><circle cx="15" cy="24" r="2.5"/><circle cx="24" cy="24" r="2.5"/><path d="M8.5 6 H12.5 M17.5 6 H21.5 M6 8.5 V12.5 M24 17.5 V21.5 M8.5 24 H12.5"/></svg></div>
  <div class="feature-label feature-label--white feature-label--recycle">Biodegradable &amp; Made From Recycled Material</div>
  <div class="feature-label feature-label--yellow feature-label--odour">Superior Odour Absorption</div>
  <div class="feature-label feature-label--white feature-label--moisture">Superior Moisture Absorption</div>
  <div class="feature-label feature-label--yellow feature-label--mineral">Special mineral technology for superior freshness.</div>
</section>

<section class="pack pack--paper">
  <div class="pack__pattern"></div>
  <div class="brand-name">PUFF'NTIDY</div>
  <div class="range-band"></div>
  <h1 class="range-title">PAPER</h1>
  <h2 class="product-line">LITTER</h2>
  <div class="cat-photo" role="img" aria-label="Photo of a ginger kitten peeking up from the bottom of the pack"></div>
  <div class="granules-photo" role="img" aria-label="Close-up photo of litter granules"></div>
  <svg class="connectors" viewBox="0 0 384 519">
    <g fill="none" stroke="#f8ea26" stroke-width="2" stroke-linecap="round">
      <path d="M110 336 Q124 346 132 344"/><path d="M127 340 L133 344 L126 348"/>
      <path d="M240 306 L254 310"/>
      <path d="M300 372 Q270 360 246 362"/><path d="M252 358 L245 362 L252 366"/>
      <path d="M148 402 Q154 390 160 384"/>
    </g>
  </svg>
  <div class="feature-icon feature-icon--recycle"><svg viewBox="0 0 30 30" fill="none" stroke="#fff" stroke-width="2" stroke-linejoin="round"><path d="M15 4 L25 22 H5 Z"/><path d="M12 18 Q15 10 20 12"/></svg></div>
  <div class="feature-icon feature-icon--odour"><svg viewBox="0 0 30 30" fill="none" stroke="#fff" stroke-width="2" stroke-linecap="round"><path d="M8 24 Q4 18 8 14 Q12 10 8 5"/><path d="M15 24 Q11 18 15 14 Q19 10 15 5"/><path d="M22 24 Q18 18 22 14 Q26 10 22 5"/></svg></div>
  <div class="feature-icon feature-icon--moisture"><svg viewBox="0 0 30 30" fill="none" stroke="#fff" stroke-width="2"><path d="M15 4 Q23 15 23 19 A8 8 0 0 1 7 19 Q7 15 15 4 Z"/></svg></div>
  <div class="feature-icon feature-icon--mineral"><svg viewBox="0 0 30 30" fill="none" stroke="#fff" stroke-width="1.6"><circle cx="6" cy="6" r="2.5"/><circle cx="15" cy="6" r="2.5"/><circle cx="24" cy="6" r="2.5"/><circle cx="6" cy="15" r="2.5"/><circle cx="24" cy="15" r="2.5"/><circle cx="6" cy="24" r="2.5"/><circle cx="15" cy="24" r="2.5"/><circle cx="24" cy="24" r="2.5"/><path d="M8.5 6 H12.5 M17.5 6 H21.5 M6 8.5 V12.5 M24 17.5 V21.5 M8.5 24 H12.5"/></svg></div>
  <div class="feature-label feature-label--white feature-label--recycle">Biodegradable &amp; Made From Recycled Material</div>
  <div class="feature-label feature-label--yellow feature-label--odour">Superior Odour Absorption</div>
  <div class="feature-label feature-label--white feature-label--moisture">Superior Moisture Absorption</div>
  <div class="feature-label feature-label--yellow feature-label--mineral">Special mineral technology for superior freshness.</div>
</section>

</body>
</html>
```